Z-Reel Carnival Podcast Cover Design

We need a podcast cover (square design) for a podcast called Z-Reel Carnival.
MANDATORY: Z-REEL CARNIVAL
OPTIONAL: with The Creature Nerd Dale Furnow

Z-Reel Carnival is a movie podcast dedicated to covering all of the cult oddities you saw in theaters and video stores as a kid but never got to rent or watch. Focusing on obscure horror, cult oddities, action movies, exploitation movies, foreign knockoffs, and more, this a show designed to help you take a trip down memory lane or find new weird movies to add to your streaming queue. Come take a walk on the wild side of cinema at Z-Reel Carnival,..where one person's trash movie is our treasure.
##
Fonts that fit the vibe we're going for:
https://www.typevault.example/sets/grindhouse-drip-font-kelvorn-studio
https://www.pinboardly.example/pin/481926035517204963/
https://www.typevault.example/sets/grindhouse-vintage-font-kelvorn-studio

Target Market(s)

Primarily male, although we have some female fans as well. Podcast fans of B-movies (inexpensively made and a bit outrageous), cult movies, weird movies, old movies, horror movies, and action films.

Industry/Entity Type

Media - Movies -Podcast

Font styles to use
Other font styles liked:
• Fonts that fit the vibe: Fonts: https://www.typevault.example/sets/grindhouse-drip-font-kelvorn-studio https://www.pinboardly.example/pin/481926035517204963/ https://www.typevault.example/sets/grindhouse-vintage-font-kelvorn-studio

Colors
EB3D1F
EC4F4E
F09395
F8D3D4
FCEDEE

Requirements
Must have
• Z-REEL CARNIVAL
Nice to have
• 1) with The Creature Nerd Dale Furnow; 2) VISUALS: VHS tapes

```html
<!DOCTYPE html>
<html lang="en">
<head>
<meta charset="utf-8">
<title>Z-Reel Carnival — Podcast Cover</title>
<link rel="stylesheet" href="https://fonts.googleapis.com/css2?family=Montserrat:wght@400;700&family=Oswald:wght@500&display=swap">
<style>
  :root {
    --ink: #08090f;
    --bone: #ffffff;
    --name-red: #d8141b;
  }
  * { margin: 0; padding: 0; box-sizing: border-box; }
  html, body { width: 1200px; height: 1200px; overflow: hidden; background: var(--ink); }
  .cover { position: relative; width: 1200px; height: 1200px; background: var(--ink); overflow: hidden; }
  .cover__art { position: absolute; inset: 0; }
  .cover__title { position: absolute; left: 0; top: 0; width: 1200px; height: 1200px; }
  .title-line {
    font-family: "Oswald", sans-serif;
    font-weight: 500;
    fill: var(--bone);
  }
  .host { position: absolute; left: 0; right: 0; text-align: center; }
  .host__tag {
    top: 935px;
    font-family: "Montserrat", sans-serif; font-size: 50px; line-height: 1;
    color: var(--bone); letter-spacing: 1px;
  }
  .host__tag strong { font-weight: 700; }
  .host__tag .light { font-weight: 400; }
  .host__name {
    top: 1010px;
    font-family: "Oswald", sans-serif; font-weight: 500; font-size: 86px;
    color: var(--name-red); letter-spacing: 12px; line-height: 1;
  }
</style>
</head>
<body>
<div class="cover">
  <svg class="cover__art" width="1200" height="1200" viewBox="0 0 1200 1200">
    <defs>
      <linearGradient id="sceneGlow" x1="0" y1="0" x2="1" y2="1">
        <stop offset="0" stop-color="#5a0306"/>
        <stop offset="0.45" stop-color="#d8070b"/>
        <stop offset="1" stop-color="#3a0204"/>
      </linearGradient>
      <linearGradient id="floorGlow" x1="0" y1="0" x2="0" y2="1">
        <stop offset="0" stop-color="#2a0a0e"/>
        <stop offset="1" stop-color="#0b0a10"/>
      </linearGradient>
    </defs>
    <rect class="bottom-band" x="0" y="850" width="1200" height="350" fill="url(#floorGlow)" role="img" aria-label="Faded haunted scene and film strip behind the host credit"/>
    <polygon class="scene" points="0,0 1095,0 445,600 445,850 0,850" fill="url(#sceneGlow)" role="img" aria-label="Grunge red sky with bats, bare branches and a haunted church silhouette"/>
    <rect class="projector" x="20" y="485" width="405" height="340" rx="18" fill="#f2eeee" role="img" aria-label="White film projector silhouette"/>
  </svg>

  <svg class="cover__title" viewBox="0 0 1200 1200" role="img" aria-label="Z-REEL CARNIVAL">
    <text class="title-line" x="478" y="637" font-size="180" textLength="620" lengthAdjust="spacingAndGlyphs">Z-REEL</text>
    <text class="title-line" x="478" y="818" font-size="180" textLength="637" lengthAdjust="spacingAndGlyphs">CARNIVAL</text>
  </svg>

  <p class="host host__tag"><span class="light">WITH THE </span><strong>CREATURE NERD</strong></p>
  <p class="host host__name">DALE FURNOW</p>
</div>
</body>
</html>
```